glow 482 is renewing its image

more dynamic website, make it look more attractive for the services we offer, at the same time more accurate on the services description. We want people to know we offer treatments that big corporations offer but not as expensive as they offer it. prices will be add by me once the website is approve

already have a website with wix.com www.glow482skin.com

Target Market(s)

women between 21 to 75

Industry/Entity Type

beauty services, body contouring

Colors

Designer to choose colors to be used in the design.

Requirements
Must have
• pictures of treatments
Nice to have
• accurate information about treatmnets, treatments menu
Should not have
• no online shopping

```html
<!DOCTYPE html>
<html lang="en">
<head>
<meta charset="utf-8">
<title>glow 482 Skin Lounge</title>
<link href="https://fonts.googleapis.com/css2?family=Roboto:wght@300;400;500;700&display=swap" rel="stylesheet">
<style>
:root{
  --blush:#fde1dd;
  --gold:#c9a070;
  --gold-line:#e9cfb3;
  --brown:#8d5b30;
  --heading-brown:#7b4519;
  --title:#b08a6a;
  --ink:#2f2f2f;
  --rule:#d9d9d9;
  --dark:#333333;
  --white:#ffffff;
}
*{margin:0;padding:0;box-sizing:border-box}
html,body{width:1200px;height:5056px;overflow:hidden}
body{position:relative;font-family:'Roboto',sans-serif;color:var(--ink);background:var(--white)}
.abs{position:absolute}
.arch-frame{position:absolute;border:2px solid var(--gold-line)}
.arch-photo{position:absolute}
.btn{position:absolute;display:flex;align-items:center;justify-content:center;background:var(--gold);color:var(--white);font-size:11px;font-weight:500;letter-spacing:.5px;border-radius:32px;text-transform:uppercase}

/* header & hero */
.hero{left:0;top:0;width:1200px;height:813px;background:var(--blush)}
.brand{left:122px;top:28px;display:flex;flex-direction:column;color:var(--gold)}
.brand-name{font-size:46px;font-weight:300;line-height:1}
.brand-tag{font-size:15px;font-weight:300;margin-left:48px;margin-top:-2px}
.nav{top:56px;font-size:12px;color:var(--ink)}
.hero-frame{left:367px;top:112px;width:463px;height:587px;border-radius:232px 232px 0 0}
.hero-photo{left:379px;top:124px;width:440px;height:563px;border-radius:220px 220px 0 0;background:linear-gradient(160deg,#f1d9c9,#e2b8a0 60%,#d6a68d)}
.hero-title{left:762px;top:286px;font-size:31px;font-weight:300;line-height:45px;color:var(--title)}
.hero-lead{left:122px;top:420px;font-size:18px;line-height:26px;color:var(--ink)}

/* services */
.section-title{left:0;width:1200px;text-align:center;font-size:33px;font-weight:300;color:var(--title)}
.body-frame{left:108px;top:1043px;width:414px;height:528px;border-radius:207px 207px 0 0}
.body-photo{left:122px;top:1056px;width:386px;height:501px;border-radius:193px 193px 0 0;background:linear-gradient(150deg,#4a2a1a,#a56c4d 55%,#d9b199)}
.group-title{font-size:23px;font-weight:700;color:var(--heading-brown)}
.treatment{font-size:17px;color:var(--ink)}
.learn{font-size:10px;font-weight:500;color:var(--gold);text-decoration:underline}
.rule{height:1px;background:var(--rule)}
.face-frame{left:664px;top:1663px;width:414px;height:524px;border-radius:207px 207px 0 0}
.face-photo{left:677px;top:1676px;width:389px;height:499px;border-radius:195px 195px 0 0;background:linear-gradient(160deg,#e6e6ea,#e9cbc4 55%,#d6b4a6)}

/* promo banner */
.promo{left:0;top:2313px;width:1200px;height:673px;background:linear-gradient(110deg,#f1efec,#e9e6e1 40%,#f4f2ef 70%,#ece6d4)}
.promo-arch{left:395px;top:2389px;width:410px;height:521px;border-radius:205px 205px 0 0;background:var(--brown)}
.promo-text{left:395px;top:2540px;width:410px;text-align:center;font-size:31px;font-weight:300;line-height:44px;color:#f3e2cf}

/* customers */
.tile{position:absolute;width:224px;height:224px}
.quote{background:var(--brown);color:var(--white);text-align:center;padding:30px 22px 0;font-size:11px;line-height:18px}
.quote strong{display:block;margin-top:14px;font-weight:500}

/* newsletter */
.news{left:0;top:3812px;width:1200px;height:676px;background:var(--blush)}
.news-frame{left:169px;top:3891px;width:408px;height:522px;border-radius:204px 204px 0 0}
.news-photo{left:181px;top:3903px;width:384px;height:498px;border-radius:192px 192px 0 0;background:linear-gradient(150deg,#f4dccd,#e2b79c 55%,#c99a84)}
.news-title{left:644px;top:4062px;font-size:31px;font-weight:300;line-height:44px;color:var(--title)}
.email{left:644px;top:4179px;width:387px;height:59px;background:var(--white);border-radius:30px;box-shadow:0 2px 6px rgba(0,0,0,.08)}
.email span{position:absolute;left:30px;top:22px;font-size:12px;color:#555}

/* footer */
.footer{left:0;top:4488px;width:1200px;height:568px;background:var(--dark);color:var(--white)}
.foot-brand{left:122px;top:4606px;color:var(--white)}
.foot-copy{left:118px;top:4706px;width:250px;font-size:11px;line-height:18px}
.foot-copy p{margin-bottom:18px}
.foot-head{top:4640px;font-size:17px;font-weight:500}
.foot-links{left:597px;top:4695px;list-style:none;font-size:11px;line-height:25px}
.social{top:4687px;width:48px;height:48px;border-radius:50%;background:var(--white)}
.social i{position:absolute;left:5px;top:5px;width:38px;height:38px;border-radius:50%}
</style>
</head>
<body>

<!-- Hero -->
<div class="abs hero"></div>
<div class="abs brand"><span class="brand-name">glow 482</span><span class="brand-tag">Skin lounge</span></div>
<span class="abs nav" style="left:788px">Home</span>
<span class="abs nav" style="left:866px">Services</span>
<span class="abs nav" style="left:960px">About</span>
<span class="abs nav" style="left:1040px">Contact</span>
<div class="arch-frame hero-frame"></div>
<div class="arch-photo hero-photo" role="img" aria-label="Photo of a woman with clear skin touching her face"></div>
<p class="abs hero-title">Let's make the most of<br>what you've got.</p>
<p class="abs hero-lead">Got the services that are designed to<br>complement your looks and needs</p>
<div class="btn" style="left:791px;top:518px;width:250px;height:63px">Book Now</div>

<!-- Services -->
<h2 class="abs section-title" style="top:938px">Services</h2>

<div class="arch-frame body-frame"></div>
<div class="arch-photo body-photo" role="img" aria-label="Photo of a body scrub treatment on a client's back"></div>
<h3 class="abs group-title" style="left:583px;top:1068px">Body Treatments</h3>
<span class="abs treatment" style="left:615px;top:1142px">Ultrasound Cavitation</span>
<span class="abs learn" style="left:1013px;top:1141px">Learn More</span>
<div class="abs rule" style="left:615px;top:1192px;width:463px"></div>
<span class="abs treatment" style="left:615px;top:1218px">Lipo-Laser</span>
<span class="abs learn" style="left:1013px;top:1217px">Learn More</span>
<div class="abs rule" style="left:615px;top:1268px;width:463px"></div>
<span class="abs treatment" style="left:615px;top:1295px">Diamond Microdermoabrasion</span>
<span class="abs learn" style="left:1013px;top:1294px">Learn More</span>
<div class="abs rule" style="left:615px;top:1345px;width:463px"></div>
<span class="abs treatment" style="left:615px;top:1371px">Vacuum Therapy</span>
<span class="abs learn" style="left:1013px;top:1370px">Learn More</span>
<div class="abs rule" style="left:615px;top:1421px;width:463px"></div>
<span class="abs treatment" style="left:615px;top:1448px">Wood Therapy</span>
<span class="abs learn" style="left:1013px;top:1447px">Learn More</span>
<div class="abs rule" style="left:615px;top:1498px;width:463px"></div>
<span class="abs treatment" style="left:615px;top:1523px">Microcurrent</span>
<span class="abs learn" style="left:1013px;top:1522px">Learn More</span>

<h3 class="abs group-title" style="left:108px;top:1800px">Facial Treatments</h3>
<span class="abs treatment" style="left:140px;top:1874px">Maximum glow 482 Natural Peel</span>
<span class="abs learn" style="left:540px;top:1873px">Learn More</span>
<div class="abs rule" style="left:140px;top:1926px;width:463px"></div>
<span class="abs treatment" style="left:140px;top:1951px">Tripolar Radio Frequency</span>
<span class="abs learn" style="left:540px;top:1950px">Learn More</span>
<div class="abs rule" style="left:140px;top:2002px;width:463px"></div>
<span class="abs treatment" style="left:140px;top:2027px">glow 482 Facials</span>
<span class="abs learn" style="left:540px;top:2026px">Learn More</span>
<div class="arch-frame face-frame"></div>
<div class="arch-photo face-photo" role="img" aria-label="Photo of a facial mask being applied with a brush"></div>

<!-- Promo -->
<div class="abs promo" role="img" aria-label="Photo of natural skincare products and cotton swabs on a white table"></div>
<div class="abs promo-arch"></div>
<p class="abs promo-text">Complete body and<br>facial treatments with<br>100% natural products<br>in a very affordable<br>price.</p>
<div class="btn" style="left:475px;top:2788px;width:250px;height:61px">Book Now</div>

<!-- Customers -->
<h2 class="abs section-title" style="top:3113px">Our Customers</h2>
<div class="tile" style="left:122px;top:3220px;background:linear-gradient(150deg,#e9dbe6,#d9a9c8)" role="img" aria-label="Photo of a client receiving a facial treatment"></div>
<div class="tile quote" style="left:365px;top:3220px">"Sed tincidunt et lacus eu sollicitudin. In vehicula justo sed efficitur ultrices. Aenean sollicitudin elit vel lectus malesuada faucibus. In bibendum ex turpis, eget lacinia felis ornare non"<strong>Customer Name</strong></div>
<div class="tile" style="left:609px;top:3220px;background:linear-gradient(150deg,#d9dde2,#b7c0c8)" role="img" aria-label="Photo of a client with a head wrap during a skin treatment"></div>
<div class="tile" style="left:852px;top:3220px;background:linear-gradient(150deg,#c8b6e0,#efd9cf)" role="img" aria-label="Photo of a device facial treatment with purple gloves"></div>
<div class="tile" style="left:122px;top:3463px;background:linear-gradient(150deg,#eeeeee,#d8c4b6)" role="img" aria-label="Photo of a body contouring treatment on the abdomen"></div>
<div class="tile" style="left:365px;top:3463px;background:linear-gradient(150deg,#cfc0b2,#8c6a55)" role="img" aria-label="Photo of two friends wearing face masks"></div>
<div class="tile" style="left:609px;top:3463px;background:linear-gradient(150deg,#8d7f78,#c9a797)" role="img" aria-label="Photo of a client wearing protective goggles during a laser treatment"></div>
<div class="tile" style="left:852px;top:3463px;background:linear-gradient(150deg,#5a4030,#c9a28a)" role="img" aria-label="Photo of a facial device treatment"></div>

<!-- Newsletter -->
<div class="abs news"></div>
<div class="arch-frame news-frame"></div>
<div class="arch-photo news-photo" role="img" aria-label="Photo of a woman holding a flower near her face"></div>
<p class="abs news-title">Get the latest updates and<br>receive exclusive discounts.</p>
<div class="abs email"><span>Your Email Address</span></div>
<div class="btn" style="left:907px;top:4179px;width:124px;height:59px">Submit</div>

<!-- Footer -->
<div class="abs footer"></div>
<div class="abs brand foot-brand"><span class="brand-name">glow 482</span><span class="brand-tag">Skin lounge</span></div>
<div class="abs foot-copy">
  <p>At glow 482 Skin Lounge we provide high quality skin and body treatments that will make you look great and feel great!</p>
  <p>With more than 10 years of experience our Esthetician Marisol will provide you with the information and the treatment that is right for you and your budget.</p>
  <p>We are like your personal assistants but for your beauty. You can always call us if you have any questions.</p>
</div>
<h4 class="abs foot-head" style="left:597px">Quick Links</h4>
<ul class="abs foot-links">
  <li>Services</li><li>About</li><li>Contact</li><li>Reservation Policy</li><li>Cancellation Policy</li>
</ul>
<h4 class="abs foot-head" style="left:870px">Follow Us</h4>
<div class="abs social" style="left:870px" role="img" aria-label="Social profile link"><i style="background:#3b5ba0"></i></div>
<div class="abs social" style="left:940px" role="img" aria-label="Social profile link"><i style="background:#c23a7a"></i></div>

</body>
</html>
```